Travinex - You are the Boss!

Travinex is a new Silicon Valley company, of the pelim founders from Berlin, which provides a "Shared Pioneer Circle". This platform allows the crowd to support startups with money, experts and fame. Our Vision is, that everyone should become an entrepreneur.

Pls find all brief details in the attached document
Updates

Would be nice to have a list of more social services I'm available on, like a list of pictograms of all my services:

Find me on: vooka, bramlet+, qrt, fenwix, moodrail, zupp, hvoxa, etc...

pls make sure to use the right font:
http://www.typemarlow.com/fonts/Velquin

Target Market(s)

Main target market is those already involved in the startup industry, by fundraising, investing, advising, cofounding and working. Travinex brings a totaly new transparency and collaborative way of starting companies to that business.

· Entrepreneurs (looking for funding, team and community)
· Investors (looking for hot investments and )
· Experts (workers looking for startups they can work for equity)
· Incubators & Business Schools (looking for tools to advise startups)

Industry/Entity Type

It Company

Requirements
Must have
• Pls find all brief details in the attached document
Nice to have

```html
<!DOCTYPE html>
<html lang="en">
<head>
<meta charset="utf-8">
<title>Travinex – Business Card</title>
<link href="https://fonts.googleapis.com/css2?family=Exo+2:wght@300;400;500;600&family=Orbitron:wght@500;700&display=swap" rel="stylesheet">
<style>
  :root {
    --stage: #3a3634;
    --card: #e4603b;
    --ink: #ffffff;
    --label: #b9b5b2;
  }
  html, body {
    margin: 0;
    padding: 0;
    width: 1018px;
    height: 1200px;
    overflow: hidden;
    background: var(--stage);
    font-family: "Exo 2", sans-serif;
    color: var(--ink);
  }
  .stage { position: relative; width: 1018px; height: 1200px; }
  .card {
    position: absolute;
    left: 95px;
    width: 834px;
    height: 482px;
    background: var(--card);
    border-radius: 48px;
  }
  .card--front { top: 78px; }
  .card--back { top: 638px; }
  .side-label {
    position: absolute;
    left: 95px;
    font-size: 18px;
    color: var(--label);
    margin: 0;
  }
  .side-label--front { top: 574px; }
  .side-label--back { top: 1136px; }

  .person { position: absolute; left: 68px; top: 72px; margin: 0; }
  .person__name {
    font-family: "Orbitron", sans-serif;
    font-weight: 700;
    font-size: 31px;
    letter-spacing: 1px;
    margin: 0;
    line-height: 1;
  }
  .person__role {
    font-size: 23px;
    font-weight: 400;
    letter-spacing: 1px;
    margin: 10px 0 0;
    line-height: 1;
  }
  .contact {
    position: absolute;
    left: 68px;
    top: 306px;
    font-size: 19px;
    font-weight: 300;
    line-height: 23px;
    margin: 0;
  }
  .social {
    position: absolute;
    left: 84px;
    top: 378px;
    list-style: none;
    margin: 0;
    padding: 0;
    font-size: 13px;
    font-weight: 300;
  }
  .social__item { display: flex; align-items: center; height: 16.5px; }
  .social__mark {
    width: 10px; height: 10px;
    background: var(--ink);
    opacity: .8;
    border-radius: 2px;
    margin-right: 23px;
  }
  .brand {
    position: absolute;
    left: 462px;
    top: 200px;
    width: 330px;
    text-align: center;
  }
  .brand__row {
    display: flex;
    align-items: center;
    justify-content: center;
    gap: 16px;
  }
  .brand__dot {
    width: 40px;
    height: 40px;
    border-radius: 50%;
    background: var(--ink);
  }
  .brand__name {
    font-family: "Exo 2", sans-serif;
    font-weight: 500;
    font-size: 44px;
    margin: 0;
    line-height: 1;
  }
  .brand__tagline { font-size: 16px; margin: 12px 0 0; line-height: 1; }

  .pitch { position: absolute; left: 0; right: 0; top: 90px; text-align: center; }
  .pitch__title { font-size: 37px; font-weight: 400; margin: 0; line-height: 1; letter-spacing: .5px; }
  .pitch__list { list-style: none; margin: 34px 0 0; padding: 0; font-size: 16px; line-height: 21.5px; }
  .pitch__cta { font-size: 19px; font-weight: 600; margin: 8px 0 0; }
  .divider {
    position: absolute;
    left: 210px;
    width: 416px;
    top: 379px;
    height: 1px;
    background: var(--ink);
  }
  .offices {
    position: absolute;
    left: 0; right: 0;
    top: 412px;
    text-align: center;
    font-size: 12px;
    line-height: 17px;
    margin: 0;
  }
</style>
</head>
<body>
<main class="stage">
  <section class="card card--front">
    <div class="person">
      <h1 class="person__name">LUKAS FERBER</h1>
      <p class="person__role">FOUNDER AND CEO</p>
    </div>
    <p class="contact">www.travinex.com<br>the@travinex.com</p>
    <ul class="social">
      <li class="social__item"><span class="social__mark"></span>chirpline.com/lukasferber</li>
      <li class="social__item"><span class="social__mark"></span>friendhall.com/lukasferber</li>
      <li class="social__item"><span class="social__mark"></span>worklinkr.com/in/lukasferber</li>
    </ul>
    <div class="brand">
      <div class="brand__row">
        <span class="brand__dot"></span>
        <p class="brand__name">Travinex</p>
      </div>
      <p class="brand__tagline">You are the Boss!</p>
    </div>
  </section>
  <p class="side-label side-label--front">Front</p>

  <section class="card card--back">
    <div class="pitch">
      <h2 class="pitch__title">Are you interested in?</h2>
      <ul class="pitch__list">
        <li>• Starting your own Business?</li>
        <li>• Investing in hot Startups?</li>
        <li>• Working for the next “Friendhall”?</li>
      </ul>
      <p class="pitch__cta">Join us on Friendhall.com/Travinex</p>
    </div>
    <div class="divider"></div>
    <p class="offices">Berlin - Kanalstraße 14 . 10969 Berlin . Germany<br>Silicon Valley - 218 Orchard Ave . Sunnyvale . CA 94086</p>
  </section>
  <p class="side-label side-label--back">Back</p>
</main>
</body>
</html>
```